Pull Up Banner Design 85cm X200cm

The pull up banner is intended for branding and services awareness purposes, and to be used at exhibition and conference. Please refer to the websites below for more information
1. https://www.brivanta.online/
2. https://www.brivanta.online/landing-page
3. https://blog.brivanta.online/faq-for-client/
4. https://blog.brivanta.online/faq-for-advisor/

Ideally, the banner will lead potential users both young entrepreneurs and online business owners (as clients) to Brivanta marketplace, and also professional services providers like accountants and finance advisors and consultants (as advisors) to sign up with the platform. (Like PixelHarbor marketplace)

Target Market(s)

Business users and accountants aged between 25 to 44 yrs old

Requirements
Must have
• website address (www.brivanta.online)
• and
• company logo "Brivanta" as attached

```html
<!DOCTYPE html>
<html lang="en">
<head>
<meta charset="utf-8">
<title>Brivanta – Pull Up Banner</title>
<link href="https://fonts.googleapis.com/css2?family=Bebas+Neue&family=Fira+Sans:wght@500;600&family=Montserrat:wght@700&display=swap" rel="stylesheet">
<style>
  :root{
    --backdrop:#c9cacc;
    --blue:#1877c1;
    --blue-deep:#1166ad;
    --sky:#4a9fdc;
    --teal-light:#bfe6e8;
    --teal:#7ccfd0;
    --heading:#c7eef6;
    --body:#b9d6e6;
    --white:#ffffff;
    --tagline:#3c5468;
    --dark:#333333;
    --url:#1d6fc0;
    --logo:#1e6fb8;
  }
  *{box-sizing:border-box;margin:0;padding:0}
  html,body{width:800px;height:1200px;overflow:hidden;background:var(--backdrop)}
  .canvas{position:relative;width:800px;height:1200px}
  .banner{
    position:absolute;left:150px;top:11px;width:618px;height:1455px;
    transform:scale(0.81);transform-origin:top left;
    background:linear-gradient(180deg,var(--sky) 0%,var(--blue) 30%,var(--blue) 100%);
    overflow:hidden;
  }
  .hero{
    position:absolute;left:-40px;top:-330px;width:698px;height:620px;
    border-radius:50%;
    background:linear-gradient(180deg,#d6f0f0 0%,var(--teal-light) 55%,var(--teal) 100%);
  }
  .logo{position:absolute;left:28px;top:22px;display:flex;flex-direction:column;align-items:center;gap:8px}
  .logo-dot{width:52px;height:52px;border-radius:50%;background:var(--logo)}
  .logo-name{font:700 30px/1 "Montserrat",sans-serif;color:var(--logo)}
  .corner{position:absolute;width:0;height:0}
  .corner-left{left:0;top:250px;border-top:70px solid transparent;border-bottom:70px solid transparent;border-left:70px solid var(--teal-light)}
  .corner-right{right:0;top:250px;border-top:70px solid transparent;border-bottom:70px solid transparent;border-right:70px solid var(--teal-light)}
  .brand-title{position:absolute;left:0;right:0;top:290px;text-align:center;font:700 72px/1 "Montserrat",sans-serif;color:var(--white)}
  .tagline{position:absolute;left:0;right:0;top:366px;text-align:center;font:400 33px/1 "Bebas Neue",sans-serif;color:var(--tagline)}
  .section-title{position:absolute;left:108px;width:402px;text-align:center;font:400 44px/1 "Bebas Neue",sans-serif;color:var(--white);padding-bottom:8px;border-bottom:1px solid var(--heading)}
  .feature{position:absolute;left:0;width:618px}
  .feature h3{position:absolute;left:100px;top:0;font:500 21px/1 "Fira Sans",sans-serif;color:var(--heading);text-transform:uppercase}
  .feature p{position:absolute;left:121px;top:27px;width:475px;font:600 18.5px/25px "Fira Sans",sans-serif;color:var(--body)}
  .icon{position:absolute}
  .icon-round{width:78px;height:78px;border-radius:50%;background:var(--teal)}
  .icon-card{border-radius:6px;background:#f5b531}
  .footer{position:absolute;left:0;top:1310px;width:618px;height:145px;background:var(--dark)}
  .footer-tri{position:absolute;bottom:0;width:0;height:0}
  .footer-tri.left{left:0;border-bottom:70px solid var(--sky);border-right:70px solid transparent}
  .footer-tri.right{right:0;border-bottom:70px solid var(--sky);border-left:70px solid transparent}
  .footer-tri.top-left{left:0;top:0;border-top:70px solid var(--sky);border-right:70px solid transparent;bottom:auto}
  .footer-tri.top-right{right:0;top:0;border-top:70px solid var(--sky);border-left:70px solid transparent;bottom:auto}
  .globe{position:absolute;left:284px;top:22px}
  .site-url{position:absolute;left:0;right:0;top:80px;text-align:center;font:400 40px/1 "Bebas Neue",sans-serif;color:var(--url)}
</style>
</head>
<body>
<div class="canvas">
  <div class="banner">
    <div class="hero" role="img" aria-label="Illustration of a smiling man working at a laptop on a desk, connected to advisor avatars in a network"></div>
    <div class="logo">
      <span class="logo-dot"></span>
      <span class="logo-name">Brivanta</span>
    </div>
    <span class="corner corner-left"></span>
    <span class="corner corner-right"></span>

    <h1 class="brand-title">Brivanta</h1>
    <p class="tagline">Matches you with the right advisors online!</p>

    <h2 class="section-title" style="top:418px">Looking for an advisor?</h2>

    <div class="feature" style="top:487px">
      <span class="icon icon-round" style="left:28px;top:46px" role="img" aria-label="Online shop icon"></span>
      <h3>One-stop borderless marketplace</h3>
      <p>Access instantly to a network of great independent advisors, consultants, industry professionals, boutique firms and small sized practices, including best talents in accounting, finance and strategy all in one place.</p>
    </div>

    <div class="feature" style="top:658px">
      <span class="icon icon-round" style="left:27px;top:14px" role="img" aria-label="Running figure icon"></span>
      <h3>Convenient and quick</h3>
      <p>Get matched instantly to 3 of the great advisors for you to compare. Then communicate, chat, interview, appoint and sign the engagement online.</p>
    </div>

    <div class="feature" style="top:781px">
      <span class="icon icon-round" style="left:27px;top:12px" role="img" aria-label="Thumbs up icon"></span>
      <h3>Hire with confidence</h3>
      <p>Explore each advisors profile and browse their previous works as well as clients review in a simple manner online.</p>
    </div>

    <h2 class="section-title" style="top:905px">Looking for a project?</h2>

    <div class="feature" style="top:979px">
      <span class="icon icon-card" style="left:41px;top:27px;width:70px;height:50px" role="img" aria-label="Profile card icon"></span>
      <h3>Professional profile</h3>
      <p>Let thousands of online users view your profile every month</p>
    </div>

    <div class="feature" style="top:1079px">
      <span class="icon" style="left:24px;top:30px;width:86px;height:70px;border-radius:6px;background:#3d82c9" role="img" aria-label="Awards and credentials icon"></span>
      <h3>Expertise showcase</h3>
      <p>Let your success cases and job credentials to be visible online. Users want to connect with you if you have relevant expertise and walked the path before.</p>
    </div>

    <div class="feature" style="top:1219px">
      <span class="icon" style="left:24px;top:46px;width:74px;height:26px;border-radius:13px;background:#3d82c9" role="img" aria-label="Job leads button icon"></span>
      <h3>Job leads</h3>
      <p>You can access to the job leads instantly at the click of a button</p>
    </div>

    <div class="footer">
      <span class="footer-tri top-left"></span>
      <span class="footer-tri top-right"></span>
      <span class="footer-tri left"></span>
      <span class="footer-tri right"></span>
      <svg class="globe" width="50" height="50" viewBox="0 0 50 50" aria-hidden="true">
        <g fill="none" stroke="#cfeff2" stroke-width="3">
          <circle cx="25" cy="25" r="22"/>
          <ellipse cx="25" cy="25" rx="10" ry="22"/>
          <line x1="3" y1="25" x2="47" y2="25"/>
          <line x1="25" y1="3" x2="25" y2="47"/>
          <path d="M7 14h36M7 36h36"/>
        </g>
      </svg>
      <p class="site-url">www.brivanta.online</p>
    </div>
  </div>
</div>
</body>
</html>
```